Onboarding project UI redesign

The web site is used to onboard clients via a video-identification process.
The end-user first tests his computer, then enters his order details and waits for an operator engagement.
When the operator engages the customer, they go through some identification steps together, ending on a contract signature page.

Target Market(s)

Finance B2C

Industry/Entity Type

Finance

Font styles to use
Sans Serif

Requirements
Must have
• Professional UI
• Design for mobile devices

```html
<!DOCTYPE html>
<html lang="en">
<head>
<meta charset="utf-8">
<title>Nordvale Bank – Waiting for operator</title>
<link rel="stylesheet" href="https://fonts.googleapis.com/css2?family=Roboto:wght@300;400&display=swap">
<style>
  :root {
    --page-bg: #f8f9fc;
    --header-bg: #ffffff;
    --header-border: #e9edf3;
    --step-active: #1a86f0;
    --step-idle: #e6edf7;
    --step-line-idle: #edf0f5;
    --title: #4a5f8f;
    --card-bg: #1f4f8c;
    --card-text: #ffffff;
    --spinner-track: #2d5c97;
    --spinner-arc: #1a86f0;
    --footer: #c4cad6;
  }
  * { box-sizing: border-box; margin: 0; padding: 0; }
  html, body {
    width: 1200px; height: 634px; overflow: hidden;
    background: var(--page-bg);
    font-family: "Roboto", sans-serif;
  }
  .screen { position: relative; width: 1200px; height: 634px; }

  .progress-header {
    position: absolute; left: 0; top: 0; width: 1200px; height: 55px;
    background: var(--header-bg);
    border-bottom: 1px solid var(--header-border);
  }
  .step {
    position: absolute; top: 19px; width: 18px; height: 18px; border-radius: 50%;
    background: var(--step-idle); color: #ffffff;
    font-size: 9px; line-height: 18px; text-align: center;
  }
  .step--active { background: var(--step-active); }
  .step-line {
    position: absolute; top: 28px; width: 82px; height: 1px;
    background: var(--step-line-idle);
  }
  .step-line--active { background: var(--step-active); }
  .step svg { display: block; margin: 4px auto 0; }

  .page-title {
    position: absolute; top: 81px; width: 100%; text-align: center;
    font-weight: 300; font-size: 15px; color: var(--title); letter-spacing: 0.2px;
  }

  .waiting-card {
    position: absolute; left: 290px; top: 146px; width: 620px; height: 408px;
    background: var(--card-bg); border-radius: 9px;
    box-shadow: 0 6px 18px rgba(31, 79, 140, 0.12);
  }
  .brand-name {
    position: absolute; top: 36px; width: 100%; text-align: center;
    font-weight: 300; font-size: 25px; color: var(--card-text); letter-spacing: 0.5px;
  }
  .spinner { position: absolute; left: 274px; top: 164px; }
  .welcome-message {
    position: absolute; top: 338px; width: 100%; text-align: center;
    font-weight: 300; font-size: 13px; color: var(--card-text);
  }

  .footer-note {
    position: absolute; top: 594px; width: 100%; text-align: center;
    font-size: 8.5px; color: var(--footer);
  }
</style>
</head>
<body>
<div class="screen">
  <header class="progress-header">
    <div class="step step--active" style="left:32px">1</div>
    <div class="step-line step-line--active" style="left:56px"></div>
    <div class="step" style="left:144px">2</div>
    <div class="step-line" style="left:168px"></div>
    <div class="step" style="left:256px">3</div>
    <div class="step-line" style="left:280px"></div>
    <div class="step" style="left:367px">4</div>
    <div class="step-line" style="left:392px"></div>
    <div class="step" style="left:479px">5</div>
    <div class="step-line" style="left:503px"></div>
    <div class="step" style="left:591px">6</div>
    <div class="step-line" style="left:615px"></div>
    <div class="step" style="left:703px">7</div>
    <div class="step-line" style="left:727px"></div>
    <div class="step" style="left:815px">8</div>
    <div class="step-line" style="left:839px"></div>
    <div class="step" style="left:927px">9</div>
    <div class="step-line" style="left:951px"></div>
    <div class="step" style="left:1039px">10</div>
    <div class="step-line" style="left:1063px"></div>
    <div class="step" style="left:1151px">
      <svg width="10" height="10" viewBox="0 0 10 10" aria-hidden="true">
        <path d="M1.5 9.5V1h7l-1.5 2.2L8.5 5.5h-7" fill="none" stroke="#ffffff" stroke-width="1"/>
      </svg>
    </div>
  </header>

  <h1 class="page-title">WAITING FOR OPERATOR</h1>

  <main class="waiting-card">
    <div class="brand-name">NORDVALE BANK</div>
    <svg class="spinner" width="72" height="72" viewBox="0 0 72 72" aria-label="Loading">
      <circle cx="36" cy="36" r="35" fill="none" stroke="var(--spinner-track)" stroke-width="1.6"/>
      <path d="M36 1 A35 35 0 0 1 71 36" fill="none" stroke="var(--spinner-arc)" stroke-width="2" stroke-linecap="round"/>
    </svg>
    <p class="welcome-message">Welcome, a few more minutes and you can activate your new Nordvale account.</p>
  </main>

  <footer class="footer-note">©2019 NORDVALE BANK</footer>
</div>
</body>
</html>
```